Software as a Service to manage Home Care Management

We need a web site designed for Home Care Management Software as a Service product, that facilitates Home Care organizations to manage and schedule carers to visit client homes. We want a modern look and feel using our existing logo.

Target Market(s)

Home Care Management organizations. Product is similar to: https://kelvantro.co/

Coding

Coded - Design and coding required

Number of Pages Required

3 page

```html
<!DOCTYPE html>
<html lang="en">
<head>
<meta charset="utf-8">
<title>Hearthline Rota – Home Care Management</title>
<link href="https://fonts.googleapis.com/css2?family=Cinzel:wght@500;600&family=Poppins:wght@400;500;600;700&display=swap" rel="stylesheet">
<style>
:root{
  --pink:#f7447f;
  --pink-soft:#f9c9d8;
  --dark:#363132;
  --darker:#2d2829;
  --ink:#222;
  --muted:#555;
  --white:#fff;
}
*{margin:0;padding:0;box-sizing:border-box}
html,body{width:1200px;height:3671px;overflow:hidden}
body{position:relative;font-family:'Poppins',sans-serif;color:var(--ink);background:var(--white)}
.abs{position:absolute}
.serif{font-family:'Cinzel',serif}

/* header */
.site-header{left:0;top:0;width:1200px;height:83px;background:var(--white);z-index:5}
.brand{left:32px;top:18px;display:flex;align-items:center;gap:10px}
.brand-dot{width:40px;height:40px;border-radius:50%;background:var(--pink)}
.brand-name{font-family:'Cinzel',serif;font-size:30px;font-weight:500;color:var(--dark);line-height:1}
.brand-tag{font-family:'Cinzel',serif;font-size:11px;letter-spacing:2px;color:var(--dark);display:block;margin-top:2px}
.main-nav{left:463px;top:32px;display:flex;gap:29px;font-size:15px;font-weight:500}
.login-btn{left:880px;top:25px;width:98px;height:34px;border:2px solid var(--dark);border-radius:17px;font-size:15px;font-weight:500;text-align:center;line-height:30px}
.demo-btn{left:1008px;top:0;width:192px;height:83px;background:var(--pink);color:var(--white);padding:18px 0 0 36px;line-height:1.1}
.demo-btn small{font-size:14px;font-weight:500;display:block}
.demo-btn strong{font-size:21px;font-weight:600}

/* hero */
.hero-photo{left:0;top:83px;width:1200px;height:830px;background:linear-gradient(100deg,#3c4250 0%,#6b6f78 35%,#a79a90 60%,#8e8680 80%,#c9c2bc 100%)}
.hero-title{left:130px;top:200px;font-family:'Cinzel',serif;font-size:58px;font-weight:600;color:var(--white);line-height:60px}
.hero-list{left:132px;top:395px;list-style:none;color:var(--white);font-size:20px}
.hero-list li{display:flex;align-items:center;gap:12px;height:37px}
.how-btn{left:132px;top:528px;width:214px;height:55px;border-radius:28px;background:var(--pink);color:var(--white);font-size:17px;font-weight:600;display:flex;align-items:center;justify-content:center;gap:8px}
.hero-curve{left:0;top:680px}

/* welcome */
.welcome-title{left:0;top:845px;width:1200px;text-align:center;font-family:'Cinzel',serif;color:var(--ink)}
.welcome-title .big{font-size:42px;display:block;line-height:48px}
.welcome-title .sub{font-size:27px;display:block}
.welcome-text{left:230px;top:940px;width:740px;text-align:center;font-size:17px;line-height:27px}
.feature{top:1052px;width:300px;text-align:center}
.feature-icon{width:86px;height:86px;border-radius:50%;border:3px solid var(--pink);margin:0 auto;display:flex;align-items:center;justify-content:center}
.feature-icon span{width:72px;height:72px;border-radius:50%;background:var(--dark);display:flex;align-items:center;justify-content:center}
.feature h3{font-family:'Cinzel',serif;font-size:21px;font-weight:600;margin-top:18px}
.feature p{font-size:13px;line-height:19px;color:var(--muted);margin:8px auto 0;width:220px}
.divider{top:1052px;width:1px;height:216px;background:#aaa}

/* services */
.services-band{left:0;top:1354px}
.service-label{color:var(--white);font-size:25px;font-weight:600;text-align:center;line-height:30px}
.service-photo{border-radius:50%}

/* what we do */
.wwd-title{left:648px;top:1808px;font-size:43px;font-weight:700;color:var(--white)}
.wwd-text{left:648px;top:1885px;width:430px;font-size:17px;line-height:24px;color:#eee}
.learn-btn{left:651px;top:2033px;width:169px;height:44px;border-radius:22px;background:var(--pink);color:var(--white);font-size:17px;font-weight:500;text-align:center;line-height:44px}

/* news */
.news-title{left:0;top:2272px;width:1200px;text-align:center;font-size:34px;font-weight:700}
.news-card{top:2351px;width:293px;height:381px;background:var(--white);box-shadow:0 2px 12px rgba(0,0,0,.1)}
.news-photo{height:171px}
.news-body{padding:20px 32px}
.news-date{color:var(--pink);font-size:14px;font-weight:500;letter-spacing:.5px}
.news-card h4{font-size:15px;font-weight:500;letter-spacing:.5px;line-height:22px;margin-top:8px}
.news-card p{font-size:14px;color:var(--muted);line-height:19px;margin-top:14px}
.news-more{color:var(--pink);font-size:13px;font-weight:600;margin-top:10px;display:block}

/* cta */
.cta-band{left:0;top:2829px;width:1200px;height:403px;background:var(--pink-soft)}
.cta-title{left:606px;top:2935px;font-size:28px;font-weight:700}
.cta-text{left:606px;top:2985px;font-size:18px;line-height:30px}
.cta-btn{left:605px;top:3065px;width:244px;height:54px;border-radius:27px;background:var(--white);font-size:17px;text-align:center;line-height:54px}

/* footer */
.site-footer{left:0;top:3231px;width:1200px;height:371px;background:var(--dark);color:var(--white)}
.foot-head{font-size:14px;font-weight:600;letter-spacing:-.3px}
.field{background:var(--white);color:#555;font-size:13px;padding:0 14px;height:36px;line-height:36px}
.send-btn{left:132px;top:3526px;width:132px;height:40px;border-radius:20px;background:var(--pink);font-size:16px;font-weight:500;text-align:center;line-height:40px;color:var(--white)}
.foot-links{list-style:none;font-size:14px;line-height:27px}
.foot-links li::before{content:"»";color:var(--pink);margin-right:6px}
.contact-row{display:flex;gap:10px;font-size:14px;line-height:19px}
.social{display:flex;gap:8px}
.social span{width:28px;height:28px;border-radius:50%;background:var(--white);border:2px solid var(--pink)}
.copyright{left:0;top:3602px;width:1200px;height:69px;background:var(--darker);color:#ddd;text-align:center;font-size:16px;line-height:69px;border-top:1px solid #555}
</style>
</head>
<body>

<header class="site-header abs">
  <div class="brand abs">
    <span class="brand-dot"></span>
    <div><span class="brand-name">Hearthline Rota</span><span class="brand-tag">HOME CARE MANAGEMENT</span></div>
  </div>
  <nav class="main-nav abs"><span>PRODUCT</span><span>PRICING</span><span>BLOG</span><span>FAQ</span><span>CONTACT</span></nav>
  <div class="login-btn abs">LOG IN</div>
  <div class="demo-btn abs"><small>BOOK A</small><strong>FREE DEMO</strong></div>
</header>

<section class="hero">
  <div class="hero-photo abs" role="img" aria-label="Smiling older couple on a sofa, one holding a phone, one wearing headphones"></div>
  <h1 class="hero-title abs">Quality care<br>from experts<br>you trust</h1>
  <ul class="hero-list abs">
    <li><svg width="22" height="22" viewBox="0 0 22 22"><circle cx="11" cy="11" r="9" fill="none" stroke="#f7447f" stroke-width="2"/><path d="M6 11l4 4 8-9" fill="none" stroke="#f7447f" stroke-width="2"/></svg>All-in-one home care software</li>
    <li><svg width="22" height="22" viewBox="0 0 22 22"><circle cx="11" cy="11" r="9" fill="none" stroke="#f7447f" stroke-width="2"/><path d="M6 11l4 4 8-9" fill="none" stroke="#f7447f" stroke-width="2"/></svg>Create staff rotas with automated scheduling tools</li>
    <li><svg width="22" height="22" viewBox="0 0 22 22"><circle cx="11" cy="11" r="9" fill="none" stroke="#f7447f" stroke-width="2"/><path d="M6 11l4 4 8-9" fill="none" stroke="#f7447f" stroke-width="2"/></svg>Easy to set up and use. Get started today!</li>
  </ul>
  <div class="how-btn abs">HOW IT WORKS <svg width="18" height="18" viewBox="0 0 18 18"><circle cx="9" cy="9" r="8" fill="#fff"/><path d="M9 5v8M5 9h8" stroke="#f7447f" stroke-width="2"/></svg></div>
  <svg class="hero-curve abs" width="1200" height="240" viewBox="0 0 1200 240">
    <path d="M0 228 C250 40 700 -20 1200 66 L1200 240 L0 240Z" fill="#363132"/>
    <path d="M0 240 C260 70 700 20 1200 80 L1200 240Z" fill="#fff"/>
  </svg>
</section>

<section class="welcome">
  <h2 class="welcome-title abs"><span class="big">Welcome to</span><span class="sub">Hearthline Rota Home Care Management</span></h2>
  <p class="welcome-text abs">Lorem Ipsum is simply dummy text of the printing and typesetting industry. Lorem Ipsum has been the industry's standard dummy text ever since the 1500s</p>

  <div class="feature abs" style="left:149px">
    <div class="feature-icon"><span><svg width="40" height="40" viewBox="0 0 40 40" fill="none" stroke="#fff" stroke-width="2"><path d="M6 8l6 6M12 8l-6 6M28 26l6 6M34 26l-6 6"/><circle cx="31" cy="11" r="4"/><circle cx="9" cy="29" r="4"/><path d="M14 11h12M26 8l3 3-3 3"/></svg></span></div>
    <h3>For Managers</h3>
    <p>Lorem Ipsum is simply dummy text of the printing and typesetting industry. Lorem Ipsum has been the industry's standard</p>
  </div>
  <div class="divider abs" style="left:449px"></div>
  <div class="feature abs" style="left:446px">
    <div class="feature-icon"><span><svg width="40" height="40" viewBox="0 0 40 40" fill="none" stroke="#fff" stroke-width="2"><circle cx="20" cy="20" r="5"/><circle cx="8" cy="8" r="3"/><circle cx="32" cy="8" r="3"/><circle cx="8" cy="32" r="3"/><circle cx="32" cy="32" r="3"/><circle cx="20" cy="5" r="2"/><circle cx="20" cy="35" r="2"/><path d="M10 10l6 6M30 10l-6 6M10 30l6-6M30 30l-6-6M20 7v8M20 25v8"/></svg></span></div>
    <h3>For Carers</h3>
    <p>Lorem Ipsum is simply dummy text of the printing and typesetting industry. Lorem Ipsum has been the industry's standard</p>
  </div>
  <div class="divider abs" style="left:748px"></div>
  <div class="feature abs" style="left:751px">
    <div class="feature-icon"><span><svg width="42" height="42" viewBox="0 0 42 42" fill="none" stroke="#fff" stroke-width="2"><circle cx="21" cy="21" r="15" stroke-dasharray="5 3"/><circle cx="21" cy="21" r="9"/><path d="M18 24v-6l3-3 3 3v6"/></svg></span></div>
    <h3>For Families</h3>
    <p>Lorem Ipsum is simply dummy text of the printing and typesetting industry. Lorem Ipsum has been the industry's standard</p>
  </div>
</section>

<section class="services">
  <svg class="services-band abs" width="1200" height="856" viewBox="0 0 1200 856">
    <path d="M0 330 C150 240 250 220 300 200 L1200 150 L1200 856 L0 856Z" fill="#363132"/>
    <path d="M0 305 C80 240 180 210 230 190 L240 220 C170 240 80 280 0 335Z" fill="#f7447f"/>
    <path d="M1030 140 C1100 150 1160 165 1200 175 L1200 160 C1150 145 1090 128 1040 120Z" fill="#f7447f"/>
  </svg>
  <div class="abs" style="left:142px;top:1372px;width:314px;height:314px;border-radius:50%;background:#363132"></div>
  <div class="abs" style="left:750px;top:1372px;width:314px;height:314px;border-radius:50%;background:#363132"></div>
  <div class="service-photo abs" role="img" aria-label="Family of three generations looking at a tablet" style="left:166px;top:1396px;width:266px;height:266px;border:4px solid #fff;background:linear-gradient(160deg,#c9b9aa,#8a7566 60%,#4b3f3a)"></div>
  <div class="service-photo abs" role="img" aria-label="Older woman in glasses smiling" style="left:774px;top:1396px;width:266px;height:266px;border:4px solid #fff;background:linear-gradient(160deg,#dfe3e6,#a9b5c2 55%,#5a6370)"></div>
  <div class="abs" style="left:425px;top:1354px;width:352px;height:352px;border-radius:50%;background:#f7447f"></div>
  <div class="service-photo abs" role="img" aria-label="Hands holding a smartphone" style="left:445px;top:1374px;width:312px;height:312px;border:5px solid #fff;background:linear-gradient(160deg,#b0a39c,#6c5b55 55%,#3a3030)"></div>
  <div class="service-label abs" style="left:166px;top:1545px;width:266px">DIGITAL<br>CARE PLANS</div>
  <div class="service-label abs" style="left:445px;top:1551px;width:312px">CALL<br>MONITORING</div>
  <div class="service-label abs" style="left:774px;top:1545px;width:266px">RISK<br>ASSESSMENTS</div>
  <svg class="abs" style="left:288px;top:1619px" width="30" height="30" viewBox="0 0 30 30"><circle cx="15" cy="15" r="13" fill="none" stroke="#f7447f" stroke-width="2"/><path d="M12 9l6 6-6 6" fill="none" stroke="#f7447f" stroke-width="2"/></svg>
  <svg class="abs" style="left:585px;top:1625px" width="30" height="30" viewBox="0 0 30 30"><circle cx="15" cy="15" r="13" fill="none" stroke="#f7447f" stroke-width="2"/><path d="M12 9l6 6-6 6" fill="none" stroke="#f7447f" stroke-width="2"/></svg>
  <svg class="abs" style="left:891px;top:1619px" width="30" height="30" viewBox="0 0 30 30"><circle cx="15" cy="15" r="13" fill="none" stroke="#f7447f" stroke-width="2"/><path d="M12 9l6 6-6 6" fill="none" stroke="#f7447f" stroke-width="2"/></svg>
</section>

<section class="what-we-do">
  <svg class="abs" style="left:0;top:1772px" width="580" height="437" viewBox="0 0 580 437">
    <path d="M0 437 L0 210 C80 60 200 0 300 0 C460 0 580 120 570 250 C560 340 500 400 470 437Z" fill="#f7447f"/>
    <path d="M0 437 L0 214 C80 66 200 6 300 6 C452 6 566 122 558 250 C550 340 492 400 460 437Z" fill="#b7aaa3" role="img" aria-label="Smiling older couple showing a phone screen"/>
    <circle cx="327" cy="223" r="38" fill="#2e2a2b"/>
    <path d="M317 205 L344 223 L317 241Z" fill="#fff"/>
  </svg>
  <h2 class="wwd-title abs">WHT WE DO?</h2>
  <p class="wwd-text abs">Lorem Ipsum is simply dummy text of the printing and typesetting industry. Lorem Ipsum has been the industry's standard dummy text ever since the 1500s, when an unknown printer took a galley of type and scrambled it to make.</p>
  <div class="learn-btn abs">Learn More</div>
</section>

<section class="news">
  <h2 class="news-title abs">LATEST NEWS</h2>
  <article class="news-card abs" style="left:132px">
    <div class="news-photo" role="img" aria-label="Older couple embracing and smiling" style="background:linear-gradient(160deg,#e6e1dc,#a89a90)"></div>
    <div class="news-body"><div class="news-date">JAN 20, 2020</div><h4>INDUSTRY'S STANDARD DUMMY TEXT EVER</h4><p>Lorem Ipsum is simply dummy text of the printing &amp; typesetting industry. Lorem Ipsum</p><span class="news-more">LEARN MORE ›</span></div>
  </article>
  <article class="news-card abs" style="left:453px">
    <div class="news-photo" role="img" aria-label="Young woman helping an older couple with a phone" style="background:linear-gradient(160deg,#eceae8,#9d948e)"></div>
    <div class="news-body"><div class="news-date">JAN 20, 2020</div><h4>INDUSTRY'S STANDARD DUMMY TEXT EVER</h4><p>Lorem Ipsum is simply dummy text of the printing &amp; typesetting industry. Lorem Ipsum</p><span class="news-more">LEARN MORE ›</span></div>
  </article>
  <article class="news-card abs" style="left:775px">
    <div class="news-photo" role="img" aria-label="Grandmother and granddaughter taking a selfie" style="background:linear-gradient(160deg,#d8dce0,#7d8a96)"></div>
    <div class="news-body"><div class="news-date">JAN 20, 2020</div><h4>INDUSTRY'S STANDARD DUMMY TEXT EVER</h4><p>Lorem Ipsum is simply dummy text of the printing &amp; typesetting industry. Lorem Ipsum</p><span class="news-more">LEARN MORE ›</span></div>
  </article>
</section>

<section class="cta">
  <div class="cta-band abs"></div>
  <svg class="abs" style="left:0;top:2829px" width="460" height="403" viewBox="0 0 460 403">
    <path d="M0 0 L380 0 C440 80 460 200 430 290 C410 340 390 380 370 403 L0 403Z" fill="#f7447f"/>
    <path d="M0 0 L370 0 C428 80 448 200 418 290 C398 340 378 380 358 403 L0 403Z" fill="#8d847f" role="img" aria-label="Smiling older couple on a sofa with a phone and headphones"/>
  </svg>
  <h2 class="cta-title abs">Want to know more?</h2>
  <p class="cta-text abs">Request a free assessment and<br>get started today</p>
  <div class="cta-btn abs">Book A Free Demo</div>
</section>

<footer class="site-footer abs">
  <div class="foot-head abs" style="left:136px;top:72px">GET IN TOUCH</div>
  <div class="field abs" style="left:132px;top:111px;width:219px">Your kid's name</div>
  <div class="field abs" style="left:361px;top:111px;width:219px">Your kid's age</div>
  <div class="field abs" style="left:132px;top:157px;width:219px">Your Email</div>
  <div class="field abs" style="left:361px;top:157px;width:219px">Phone Number</div>
  <div class="field abs" style="left:132px;top:203px;width:448px;height:72px">Your Message</div>

  <div class="foot-head abs" style="left:649px;top:72px">QUICK LINKS</div>
  <ul class="foot-links abs" style="left:649px;top:104px"><li>Product</li><li>Pricing</li><li>Blog</li><li>FAQ</li><li>Contact Us</li></ul>

  <div class="foot-head abs" style="left:834px;top:72px">QUICK LINKS</div>
  <div class="contact-row abs" style="left:834px;top:106px"><svg width="16" height="18" viewBox="0 0 16 18"><path d="M8 17s6-6 6-10A6 6 0 0 0 2 7c0 4 6 10 6 10z" fill="none" stroke="#f7447f" stroke-width="1.6"/><circle cx="8" cy="7" r="2" fill="#f7447f"/></svg><span>Hearthline Rota<br>Home Care Management</span></div>
  <div class="contact-row abs" style="left:834px;top:162px"><svg width="16" height="16" viewBox="0 0 16 16"><path d="M3 1l3 3-2 2c1 2 3 4 5 5l2-2 3 3-2 3C7 14 2 9 1 3z" fill="#f7447f"/></svg><span>(305) 555-0147</span></div>
  <div class="contact-row abs" style="left:834px;top:200px"><svg width="16" height="14" viewBox="0 0 16 14"><rect x="1" y="2" width="14" height="10" fill="none" stroke="#f7447f" stroke-width="1.4"/><path d="M1 2l7 6 7-6" fill="none" stroke="#f7447f" stroke-width="1.4"/></svg><span>contact@hearthline-mail.com</span></div>

  <div class="foot-head abs" style="left:649px;top:274px">STAY CONNECTED</div>
  <div class="social abs" style="left:799px;top:268px"><span></span><span></span><span></span><span></span></div>
</footer>
<div class="send-btn abs">Send Us</div>

<div class="copyright abs">© 2020 Hearthline Rota | All Rights are Reserved | Terms and Conditions</div>

</body>
</html>
```